Rather Likely The Brightest Venture
Website for Life Coach
Rather Likely The Brightest Venture - Personal Care
Creative Brief
Personal Care
www.bluelanternhour.com
Website design for inspirational and motivational training company. Initial focus of the website is to promote trainer for life coach and inspirational speaker engagements with plan to expend into seminar and web based trainings in 2013.
General feel to be very upbeat, happy, feel good, simple and easy to navigate. !!When referring to the holding page of Blue Lantern Hour (which I think looks crap) please note the writing in the Logo of the name should be in Black!!
left side
http://www.quostelbury.com/
http://www.drwabble.com/
http://www.nora-pellham.com/
Home page to include areas for the following: Top banner showing logo, quote and small picture of face of company. Below this a thicker banner with sunflower field picture (in future to be a video link) and beside it text of an inspirational quote that will change on a regular basis. This to also include an opt in button where they can provide email address to be contacted or receive blogs and articles direct to their account. Links to other pages: home, the way, live it, who is he, contact me, archive Home page to also include a Short text intro to what blue lantern hour is all about with a picture of face of company again. Below this Space for most recent blog or article in full (to be changed on a regular basis) Opt in button at bottom of page Links at bottom of page to affiliated websites The opt in button to be at top and bottom of all pages with affiliate web links at bottom of all pages. Additional pages: The Way: A page describing the lifestyle being coached and it's different sections. There are 6 text sections in total on this page, each with a matching inspirational image to it. Live It: Introducing the concept of coaching. Images and text again with one testimonial at the top and a list of testimonials at the bottom Who Is He: A simply text and images page for bio information Contact: listing of ways in which to contact me. Also a space where they can fill out name, contact, and question or request. The submit button will automatically send this to an email. Archive: a simple listing of previous blogs and articles. These to be listed at top with a click on link to where they are further down the page

```html
<!DOCTYPE html>
<html lang="en">
<head>
<meta charset="utf-8">
<title>Blue Lantern Hour</title>
<link href="https://fonts.googleapis.com/css2?family=Oswald:wght@500;700&family=Arimo:wght@400;700&display=swap" rel="stylesheet">
<style>
:root{
  --bg:#cfe79b;
  --bg-light:#e3f2b8;
  --panel:#ffffff;
  --panel-edge:#eef6d9;
  --green:#6fb324;
  --green-dark:#4f8f12;
  --green-light:#96cf3c;
  --yellow:#f3e400;
  --yellow-soft:#f8f08a;
  --logo:#cdb514;
  --text:#555555;
  --text-dark:#333333;
  --muted:#888888;
  --line:#dcdcdc;
}
*{box-sizing:border-box;margin:0;padding:0}
html,body{width:1200px;height:1072px;overflow:hidden}
body{
  position:relative;
  background:radial-gradient(ellipse at 50% 30%,var(--bg-light),var(--bg) 70%);
  font-family:"Arimo",Arial,sans-serif;color:var(--text);
}
.abs{position:absolute}
.top-actions{top:8px;left:893px;display:flex;gap:14px}
.top-actions a{display:block;width:52px;height:20px;border-radius:4px;background:linear-gradient(var(--green-light),var(--green));color:#fff;font-size:9px;font-weight:700;text-align:center;line-height:20px;text-decoration:none;text-transform:uppercase}
.page{top:96px;left:180px;width:843px;height:855px;background:var(--panel);border:4px solid var(--panel-edge)}
.logo{top:30px;left:36px;font-family:"Oswald",sans-serif;font-weight:700;font-size:34px;color:var(--logo);letter-spacing:1px}
.nav{top:94px;left:0;width:835px;height:32px;background:linear-gradient(var(--green-light),var(--green));display:flex}
.nav a{color:#fff;font-size:11px;font-weight:700;text-transform:uppercase;text-decoration:none;line-height:32px;position:absolute}
.hero{top:126px;left:0;width:835px;height:273px;background:linear-gradient(180deg,#f7ec2a,var(--yellow) 60%,#eadb00)}
.hero-photo{top:18px;left:82px;width:260px;height:255px;background:linear-gradient(180deg,#e9dc44,#3d3d3d 70%,#2b2b2b);border-radius:6px 6px 0 0}
.hero-quote{top:29px;left:310px;width:507px;height:140px;background:var(--yellow-soft);padding:16px 18px}
.hero-quote h2{font-family:"Oswald",sans-serif;font-weight:500;font-size:17px;color:var(--green-dark);text-transform:uppercase;margin-bottom:6px}
.hero-quote p{font-size:13px;line-height:17px;color:var(--text)}
.video{top:428px;left:14px;width:510px;height:147px;background:linear-gradient(180deg,#3a6fae,#7aa64a 45%,#e5b512 75%,#5c7a22)}
.video .play{top:45px;left:230px}
.video .caption{bottom:0;left:0;width:100%;height:30px;background:rgba(20,40,70,.75);color:#fff;font-family:"Oswald",sans-serif;font-size:14px;text-align:center;line-height:30px;text-transform:uppercase}
h3.section{font-family:"Oswald",sans-serif;font-weight:500;font-size:17px;color:var(--green);text-transform:uppercase}
.newsletter{top:428px;left:547px;width:272px}
.newsletter input{display:block;margin-top:10px;width:272px;height:26px;border:1px solid var(--line);padding:0 8px;font:11px "Arimo",Arial,sans-serif;color:var(--muted)}
.newsletter p{font-size:11px;line-height:14px;margin-top:8px}
.newsletter button{margin-top:8px;width:90px;height:28px;border:0;border-radius:3px;background:linear-gradient(var(--green-light),var(--green));color:#fff;font-family:"Oswald",sans-serif;font-size:15px;text-transform:uppercase}
.divider{top:592px;left:14px;width:805px;height:1px;background:var(--line)}
.news{top:600px;left:14px;width:500px}
.news-item{margin-top:12px}
.news-item .date{font-size:10px;color:var(--muted)}
.news-item h4{font-size:14px;font-weight:400;color:var(--green);margin:3px 0}
.news-item p{font-size:11px;line-height:15px}
.read-more{top:826px;left:440px;font-size:11px;color:var(--text-dark)}
.tweets{top:600px;left:547px;width:272px}
.tweets h3{display:flex;align-items:center;gap:8px}
.tweet{display:flex;gap:14px;margin-top:22px}
.tweet .avatar{flex:none;width:55px;height:52px;border-radius:8px;background:var(--green)}
.tweet p{font-size:10px;line-height:13px}
.tweet a{color:var(--green);font-size:10px}
.tweet small{display:block;font-size:9px;color:var(--muted)}
.join{top:826px;left:680px;font-size:11px;color:var(--green)}
.footer-nav{top:972px;left:183px;font-size:15px;color:var(--text-dark)}
.footer-nav span{color:var(--muted);margin:0 10px}
.copyright{top:1012px;left:262px;font-size:9px;color:var(--muted)}
.follow{top:968px;left:860px;font-size:15px;color:var(--text-dark);text-transform:uppercase}
.follow .marks{display:flex;gap:6px;margin-top:6px}
.follow .marks i{display:block;width:22px;height:22px;border-radius:3px;background:var(--green-dark)}
</style>
</head>
<body>
<div class="abs top-actions"><a href="#">Login</a><a href="#">Sign up</a></div>

<div class="abs page">
  <div class="abs logo">BLUE LANTERN HOUR</div>
  <nav class="abs nav">
    <a href="#" style="left:48px">Home</a>
    <a href="#" style="left:172px">The Way</a>
    <a href="#" style="left:330px">Live It</a>
    <a href="#" style="left:500px">Who Is He</a>
    <a href="#" style="left:700px">Contact Me</a>
  </nav>

  <section class="abs hero">
    <div class="abs hero-photo" role="img" aria-label="Portrait of the coach speaking at a microphone"></div>
    <div class="abs hero-quote">
      <h2>Lorem ipsum dolor sit amet, consectetuer adipiscing</h2>
      <p>Lorem ipsum dolor sit amet, consectetuer adipiscing elit. Nam cursus. Morbi ut mi. Nullam enim leo, egestas id, condimentum at, laoreet mattis, massa. Sed eleifend nonummy diam Lorem ipsum dolor sit amet</p>
    </div>
  </section>

  <div class="abs video" role="img" aria-label="Sunflower field under a blue sky, video preview">
    <svg class="abs play" width="50" height="50" viewBox="0 0 50 50"><rect width="50" height="50" rx="6" fill="rgba(0,0,0,.55)"/><path d="M19 14 L36 25 L19 36 Z" fill="#fff"/></svg>
    <div class="abs caption">Lorem ipsum dolor sit amet, consectetuer adipiscing elit.</div>
  </div>

  <section class="abs newsletter">
    <h3 class="section">Newsletter</h3>
    <input type="text" value="Enter Your Email ID" aria-label="Email">
    <p>Lorem ipsum dolor sit amet, consectetuer adipiscing elit.</p>
    <button>Submit</button>
  </section>

  <div class="abs divider"></div>

  <section class="abs news">
    <h3 class="section">Latest News</h3>
    <article class="news-item">
      <div class="date">24 JUN 2012</div>
      <h4>Lorem ipsum dolor sit amet, consectetuer adipiscing elit</h4>
      <p>Lorem ipsum dolor sit amet, consectetuer adipiscing elit. Nam cursus. Morbi ut mi. Nullam enim leo, egestas id, condimentum at, laoreet mattis, massa. Sed eleifend nonummy diam. Praesent mauris ante, elementum et, bibendum at, posuere sit amet, nibh. Duis tincidunt lectus quis dui viverra vestibulum.</p>
    </article>
    <article class="news-item">
      <div class="date">24 JUN 2012</div>
      <h4>Lorem ipsum dolor sit amet, consectetuer adipiscing elit</h4>
      <p>Lorem ipsum dolor sit amet, consectetuer adipiscing elit. Nam cursus. Morbi ut mi. Nullam enim leo, egestas id, condimentum at, laoreet mattis, massa. Sed eleifend nonummy diam. Praesent mauris ante, elementum et, bibendum at, posuere sit amet, nibh. Duis tincidunt lectus quis dui viverra vestibulum.</p>
    </article>
  </section>
  <a class="abs read-more" href="#">read more..</a>

  <section class="abs tweets">
    <h3 class="section"><svg width="18" height="18"><circle cx="9" cy="9" r="8" fill="var(--green)"/></svg>Tweets</h3>
    <div class="tweet">
      <div class="avatar"></div>
      <div><p>Lorem ipsum dolor sit amet, consectetuer adipiscing elit. Nam cursus. Morbi ut mi.</p><a href="#">Lorem ipsum dolor sit amet</a><small>10 minutes ago</small></div>
    </div>
    <div class="tweet">
      <div class="avatar"></div>
      <div><p>Lorem ipsum dolor sit amet, consectetuer adipiscing elit. Nam cursus. Morbi ut mi.</p><a href="#">Lorem ipsum dolor sit amet</a><small>10 minutes ago</small></div>
    </div>
  </section>
  <a class="abs join" href="#">Join the conversation</a>
</div>

<nav class="abs footer-nav">Home<span>|</span>the way<span>|</span>live it<span>|</span>who is he<span>|</span>Contact me</nav>
<div class="abs copyright">COPYRIGHT@2012 BLUE LANTERN HOUR. ALL RIGHTS RESERVED</div>
<div class="abs follow">Follow us on
  <div class="marks"><i></i><i></i><i></i><i></i></div>
</div>
</body>
</html>
```